Salon and Spa Distributor Business Card

Need a business card. We are are distributor in the salon and spa industry. We identify with natural beauty. Need a card with:
Company Name: Petal Haven"
Title: "President & CEO"
Address
Company Phone number
email
website
Tag Line:" The Professional Salon Source"

Industry/Entity Type

Business

Contact Information for Business Card

Name: Lena Morcott
Title: "President & CEO"
Address: 317 Birchfield Ln, Oakvane, NJ 07481
Company Phone number: 800-463-9152
email: lenamorcott@petalhaven-example.com
website: www.petalhaven-example.com

Requirements
Should not have
• No black backgrounds

```html
<!DOCTYPE html>
<html lang="en">
<head>
<meta charset="utf-8">
<title>Petal Haven — Business Card</title>
<link rel="stylesheet" href="https://fonts.googleapis.com/css2?family=Questrial&display=swap">
<style>
  :root {
    --page-bg: #ece7df;
    --card-bg: #f4f2ee;
    --card-edge: #d9d6cf;
    --green-dark: #1f6e2a;
    --green-mid: #2f8f2e;
    --green-bright: #55b032;
    --text-grey: #4a4a45;
    --tagline: #d5ebc0;
  }
  * { box-sizing: border-box; margin: 0; padding: 0; }
  html, body {
    width: 1200px;
    height: 1010px;
    overflow: hidden;
    background: var(--page-bg);
    font-family: "Questrial", "Century Gothic", sans-serif;
  }
  .business-card {
    position: absolute;
    left: 160px;
    top: 250px;
    width: 880px;
    height: 510px;
    background: var(--card-bg);
    border: 1px solid var(--card-edge);
    box-shadow: 0 10px 30px rgba(60, 50, 40, 0.12);
    overflow: hidden;
  }
  .brand-mark {
    position: absolute;
    left: 70px;
    top: 150px;
    width: 250px;
    display: flex;
    align-items: center;
    gap: 14px;
  }
  .brand-mark-dot {
    width: 40px;
    height: 40px;
    border-radius: 50%;
    background: var(--green-mid);
    flex: none;
  }
  .brand-mark-name {
    font-size: 30px;
    color: var(--green-mid);
    white-space: nowrap;
  }
  .contact-block {
    position: absolute;
    left: 428px;
    top: 112px;
  }
  .company-name {
    font-size: 38px;
    font-weight: 400;
    color: var(--green-dark);
    line-height: 1.1;
  }
  .job-title {
    font-size: 17px;
    color: var(--text-grey);
    margin-top: 2px;
  }
  .contact-list {
    list-style: none;
    margin-top: 34px;
  }
  .contact-list li {
    display: flex;
    align-items: center;
    gap: 18px;
    font-size: 21px;
    color: var(--text-grey);
    height: 31px;
  }
  .contact-icon {
    width: 20px;
    height: 20px;
    flex: none;
  }
  .contact-list .address {
    gap: 0;
    margin-top: 2px;
  }
  .footer-band {
    position: absolute;
    left: 0;
    bottom: 0;
    width: 880px;
    height: 68px;
  }
  .tagline {
    position: absolute;
    left: 428px;
    bottom: 14px;
    font-size: 21px;
    color: var(--tagline);
  }
</style>
</head>
<body>
  <main class="business-card">
    <div class="brand-mark">
      <span class="brand-mark-dot"></span>
      <span class="brand-mark-name">Petal Haven</span>
    </div>

    <section class="contact-block">
      <h1 class="company-name">Petal Haven</h1>
      <p class="job-title">President &amp; CEO</p>
      <ul class="contact-list">
        <li>
          <svg class="contact-icon" viewBox="0 0 20 20" aria-hidden="true">
            <path fill="var(--green-dark)" d="M2 7c0-2 3-4 8-4s8 2 8 4v2h-4V7.5c-1-.6-2.4-1-4-1s-3 .4-4 1V9H2z"/>
            <path fill="var(--green-dark)" d="M4 11h12l1 6H3z"/>
          </svg>
          800-463-9152
        </li>
        <li>
          <svg class="contact-icon" viewBox="0 0 20 20" aria-hidden="true">
            <rect x="1" y="4" width="18" height="12" fill="var(--green-dark)"/>
            <path d="M1.5 4.5 10 11l8.5-6.5" fill="none" stroke="var(--card-bg)" stroke-width="1.4"/>
          </svg>
          lenamorcott@petalhaven-example.com
        </li>
        <li>
          <svg class="contact-icon" viewBox="0 0 20 20" aria-hidden="true">
            <circle cx="10" cy="10" r="8.5" fill="var(--green-dark)"/>
            <g fill="none" stroke="var(--card-bg)" stroke-width="1">
              <ellipse cx="10" cy="10" rx="3.5" ry="8.5"/>
              <path d="M1.5 10h17M3 6h14M3 14h14"/>
            </g>
          </svg>
          www.petalhaven-example.com
        </li>
        <li class="address">317 Birchfield Ln, Oakvane, NJ 07481</li>
      </ul>
    </section>

    <svg class="footer-band" viewBox="0 0 880 68" aria-hidden="true">
      <defs>
        <linearGradient id="band-light" x1="0" x2="1" y1="0" y2="0">
          <stop offset="0" stop-color="#4aa82c"/>
          <stop offset="1" stop-color="#6cc13a"/>
        </linearGradient>
        <linearGradient id="band-dark" x1="0" x2="1" y1="0" y2="0">
          <stop offset="0" stop-color="#1d7a2a"/>
          <stop offset="1" stop-color="#1a6a26"/>
        </linearGradient>
      </defs>
      <rect x="0" y="32" width="400" height="36" fill="url(#band-light)"/>
      <polygon points="336,68 374,0 880,0 880,68" fill="url(#band-dark)"/>
    </svg>
    <p class="tagline">The Professional Salon Source</p>
  </main>
</body>
</html>
```